Re-design of veterinary clinic website *

For a future relaunch of our webpage, we would like to find a fresh design that still incorporates the spirit of our current one which can be found at http://dr-wenzlaff.de
We are a small business that appeals to locals but are known in a wide area for specialist services.
According to analytics data, most people rarely read through the full website but are using it to inform themselves about opening hours, Telephone numbers and location. Still, the website needs to offer enough content to be ranked positively by the Quandle algorithm.
Our logo is not part of the re-design but needs to be included in your proposal as is. It can be used a source of inspiration, just as the current design. Keep in mind, that the design will be used as the basis of a fluid webdesign for both mobile and desktop. Roughly 75% of our users are on mobile devices.
Target Market(s)
Locals
Industry/Entity Type
Veterinary
Number of Pages Required
1 page
Look and feel
Each slider illustrates characteristics of the customer's brand and the style your logo design should communicate.

```html
<!DOCTYPE html>
<html lang="en">
<head>
<meta charset="utf-8">
<title>Jonas Falkenrath Veterinary</title>
<link href="https://fonts.googleapis.com/css2?family=Open+Sans:wght@400;600;700;800&display=swap" rel="stylesheet">
<style>
:root{
  --navy:#26346e;
  --blue:#3b4c9b;
  --ink:#2a2f3a;
  --muted:#8a8f99;
  --soft:#f2f4f8;
  --line:#e2e5eb;
  --warm:#f7f1ea;
  --dark:#222428;
  --white:#ffffff;
}
*{box-sizing:border-box;margin:0;padding:0}
html,body{width:699px;height:1200px;overflow:hidden}
body{font-family:"Open Sans",Arial,sans-serif;color:var(--ink);background:var(--white);font-size:6px;line-height:1.5}
.wrap{width:432px;margin:0 auto;position:relative}

.topbar{height:23px;border-bottom:1px solid var(--line);display:flex;align-items:center}
.topbar .wrap{display:flex;justify-content:space-between;align-items:center;font-size:5.5px;color:var(--muted)}
.topbar .info span{margin-right:14px}
.topbar .right{display:flex;gap:5px;align-items:center}
.dot{width:6px;height:6px;border-radius:50%;background:var(--muted);display:inline-block}

.nav{height:31px;display:flex;align-items:center}
.nav .wrap{display:flex;justify-content:space-between;align-items:center}
.brand{display:flex;align-items:center;gap:4px;font-weight:700;font-size:8px;color:var(--navy)}
.brand i{width:8px;height:8px;background:var(--navy);display:inline-block}
.menu{display:flex;gap:13px;font-size:5.5px;color:var(--ink)}

.hero{height:268px;background:linear-gradient(90deg,#f6f7f9 0%,#eef0f3 45%,#e6e9ee 100%);position:relative;overflow:hidden}
.hero .photo{position:absolute;right:0;top:0;width:330px;height:100%;background:linear-gradient(160deg,#e9edf2 0%,#d3dbe6 40%,#b8c7d9 70%,#cfd5da 100%)}
.hero .copy{position:absolute;left:135px;top:78px;width:270px}
.hero h1{font-size:22px;line-height:1.2;font-weight:700;color:var(--navy);margin-bottom:8px}
.hero p{font-size:5px;color:#555;margin-bottom:10px;width:230px}
.btn{display:inline-block;background:var(--navy);color:var(--white);font-size:5.5px;padding:5px 14px;border-radius:10px}
.hero .dots{position:absolute;left:346px;bottom:10px;display:flex;gap:4px}
.hero .dots b{width:4px;height:4px;border-radius:50%;background:#c9ccd2}
.hero .dots b:first-child{background:var(--navy)}

.services{height:210px;background:var(--soft);text-align:center;padding-top:24px}
.services h2{font-size:11px;color:var(--navy);font-weight:700}
.services .rule{width:30px;height:1px;background:var(--navy);margin:3px auto 5px}
.services .lead{width:280px;margin:0 auto 12px;font-size:4.5px;color:var(--muted)}
.cards{display:flex;justify-content:center;gap:8px}
.card{width:88px;height:108px;background:var(--white);border:1px solid var(--line);padding:12px 8px}
.card svg{width:16px;height:16px;margin-bottom:5px}
.card h3{font-size:6px;color:var(--navy);margin-bottom:4px}
.card p{font-size:4.5px;color:var(--muted);margin-bottom:6px}
.card a{font-size:4.5px;color:var(--navy);text-decoration:none}

.welcome{height:182px;display:flex;align-items:center}
.welcome .wrap{display:flex;gap:10px;align-items:center}
.pets{width:205px;height:140px;background:radial-gradient(ellipse at 55% 55%,#e9c49a 0%,#d9a06c 35%,#f6f1ea 72%,#ffffff 100%)}
.welcome .text{width:217px}
.welcome h2{font-size:8.5px;color:var(--navy);margin-bottom:6px}
.welcome p{font-size:4.8px;color:#555;margin-bottom:6px}

.hours{height:152px;display:flex}
.hours .table{width:292px;background:var(--warm);padding:12px 0 0 145px}
.hours h2{font-size:11px;color:var(--ink);margin-bottom:2px;white-space:nowrap}
.hours .rule{width:30px;height:1px;background:var(--navy);margin-bottom:5px}
.hours table{border-collapse:collapse;font-size:4.5px;width:120px}
.hours td{padding:2.5px 0;border-bottom:1px solid #eadfd2;white-space:nowrap}
.hours .owner{flex:1;background:linear-gradient(110deg,#f3ece4 0%,#c9a98b 35%,#8a6a55 55%,#e4ddd6 100%)}

.contact{height:254px;display:flex}
.contact .left{width:292px;padding:24px 0 0 190px}
.contact .right{flex:1;background:var(--soft);padding:24px 0 0 8px;position:relative}
.keep{font-size:8px;font-weight:800;line-height:1.1;color:var(--ink);white-space:nowrap}
.cols{display:flex;gap:14px}
.cinfo{width:78px;font-size:4.5px;color:#555}
.cinfo h3,.form h3{font-size:5.5px;color:var(--ink);margin-bottom:4px}
.cinfo p{margin-bottom:4px}
.form{width:170px}
.form .row{display:flex;gap:5px}
.form .fields{width:55px}
.field{height:10px;border:1px solid var(--line);background:var(--white);margin-bottom:4px;font-size:4px;color:var(--muted);padding:1px 3px}
.msg{flex:1;height:38px;border:1px solid var(--line);background:var(--white);font-size:4px;color:var(--muted);padding:2px 3px}
.send{float:right;background:var(--navy);color:var(--white);font-size:5px;padding:2px 12px;margin-top:2px}
.map{position:absolute;left:8px;top:130px;width:262px;height:90px;background:linear-gradient(135deg,#eef0ec,#e3e7e4 50%,#dfe4ea);border:1px solid var(--line)}

.footer{height:80px;background:var(--dark);text-align:center;color:#bfc2c8;font-size:5px;padding-top:22px}
.footer .social{display:flex;justify-content:center;gap:5px;margin-top:8px}
.footer .social span{width:9px;height:9px;border-radius:50%;background:var(--blue)}
</style>
</head>
<body>
<header>
  <div class="topbar">
    <div class="wrap">
      <div class="info"><span>&#9993; info@tierarzt-falkenrath.de</span><span>&#9742; +49 4321 55 870</span></div>
      <div class="right"><span>Deutsch</span><span class="dot"></span><span class="dot"></span><span class="dot"></span></div>
    </div>
  </div>
  <nav class="nav">
    <div class="wrap">
      <div class="brand"><i></i>Jonas Falkenrath</div>
      <div class="menu"><span>Home</span><span>Practice</span><span>Team</span><span>Office hours</span><span>Services</span><span>Contact</span></div>
    </div>
  </nav>
</header>

<section class="hero">
  <div class="photo" role="img" aria-label="Veterinarian holding a dog in a bright clinic room"></div>
  <div class="copy">
    <h1>Lorem ipsum dolor sit amet consectetur</h1>
    <p>Sed ut perspiciatis unde omnis iste natus error sit voluptatem accusantium doloremque laudantium, totam rem aperiam eaque ipsa quae ab illo inventore.</p>
    <span class="btn">More information</span>
  </div>
  <div class="dots"><b></b><b></b></div>
</section>

<section class="services">
  <h2>Our Services</h2>
  <div class="rule"></div>
  <p class="lead">Lorem ipsum dolor sit amet, consectetur adipiscing elit sed do eiusmod tempor incididunt ut labore et dolore magna aliqua enim ad minim.</p>
  <div class="cards">
    <div class="card">
      <svg viewBox="0 0 20 20" fill="none" stroke="#26346e" stroke-width="1.2"><circle cx="10" cy="11" r="6"/><path d="M5 6 3 3M15 6l2-3"/><circle cx="8" cy="10" r=".6"/><circle cx="12" cy="10" r=".6"/></svg>
      <h3>Dogs</h3>
      <p>Ut enim ad minima veniam quis nostrum exercitationem ullam corporis suscipit.</p>
      <a>Learn more &rsaquo;</a>
    </div>
    <div class="card">
      <svg viewBox="0 0 20 20" fill="none" stroke="#26346e" stroke-width="1.2"><path d="M4 4l3 3h6l3-3v8a6 6 0 0 1-12 0z"/><circle cx="8" cy="11" r=".6"/><circle cx="12" cy="11" r=".6"/></svg>
      <h3>Cats</h3>
      <p>Quis autem vel eum iure reprehenderit qui in ea voluptate velit esse quam.</p>
      <a>Learn more &rsaquo;</a>
    </div>
    <div class="card">
      <svg viewBox="0 0 20 20" fill="none" stroke="#26346e" stroke-width="1.2"><ellipse cx="10" cy="12" rx="6" ry="5"/><circle cx="6" cy="6" r="2"/><circle cx="14" cy="6" r="2"/></svg>
      <h3>Small Mammals</h3>
      <p>At vero eos et accusamus et iusto odio dignissimos ducimus qui blanditiis.</p>
      <a>Learn more &rsaquo;</a>
    </div>
  </div>
</section>

<section class="welcome">
  <div class="wrap">
    <div class="pets" role="img" aria-label="Puppy and kitten sitting together"></div>
    <div class="text">
      <h2>Welcome to Jonas Falkenrath Veterinary</h2>
      <p>Nemo enim ipsam voluptatem quia voluptas sit aspernatur aut odit aut fugit, sed quia consequuntur magni dolores eos qui ratione voluptatem sequi nesciunt neque porro quisquam.</p>
      <p>Lorem ipsum dolor sit amet, consectetur adipiscing elit. Nulla facilisi morbi tempus iaculis urna id volutpat lacus laoreet non curabitur gravida.</p>
      <span class="btn">Read more</span>
    </div>
  </div>
</section>

<section class="hours">
  <div class="table">
    <h2>Opening Hours</h2>
    <div class="rule"></div>
    <table>
      <tr><td>Monday</td><td>9:00</td><td>12:00</td><td>15:00</td><td>18:00</td></tr>
      <tr><td>Tuesday</td><td>9:00</td><td>12:00</td><td>15:00</td><td>18:00</td></tr>
      <tr><td>Wednesday</td><td>9:00</td><td>12:00</td><td>15:00</td><td>18:00</td></tr>
      <tr><td>Thursday</td><td>9:00</td><td>12:00</td><td>Closed</td><td></td></tr>
      <tr><td>Friday</td><td>9:00</td><td>12:00</td><td>15:00</td><td>18:00</td></tr>
      <tr><td>Saturday</td><td>10:00</td><td>12:00</td><td>Closed</td><td></td></tr>
      <tr><td>Sunday</td><td>Closed</td><td></td><td></td><td></td></tr>
    </table>
  </div>
  <div class="owner" role="img" aria-label="Woman hugging her small dog"></div>
</section>

<section class="contact">
  <div class="left">
    <div class="keep">KEEP<br>IN TOUCH</div>
  </div>
  <div class="right">
    <div class="cols">
      <div class="cinfo">
        <h3>Contact Info</h3>
        <p>Tierarztpraxis Falkenrath<br>Mühlenstraße 8<br>24530 Lindenfeld</p>
        <p><b>Email:</b> info@tierarzt-falkenrath.de<br><b>Tel:</b> +49 4321 55 870<br><b>Fax:</b> +49 4321 55 871</p>
      </div>
      <div class="form">
        <h3>Contact Us</h3>
        <div class="row">
          <div class="fields"><div class="field">Name</div><div class="field">Email</div><div class="field">Phone</div></div>
          <div class="msg">Message</div>
        </div>
        <span class="send">Send</span>
      </div>
    </div>
    <div class="map" role="img" aria-label="Street map showing the clinic location"></div>
  </div>
</section>

<footer class="footer">
  <p>Copyright &copy; 2018 Dr. Falkenrath. All rights reserved.</p>
  <div class="social"><span></span><span></span><span></span></div>
</footer>
</body>
</html>
```